Corvel Lane

Small ageny public transit advocacy, funding and compliance.
Consulting and lobbying efforts for small public transit agencies and communities exploring public transit opportunities.
Updates

I was interested in a simple line sketch suggesting motion, mobility. The card will be black on white. I would like it to include the bUs ones brief; Advocacy, Funding , and Compliance for small transit agencies.

Reason: I have been traveling and have had limited time to respond. Thank you all for your submit talks.

Industry/Entity Type

Consulting

Contact Information for Business Card

Mark D Loyer
Phone (614) 380-2917
Email markdloyer@vantomail.test

```html
<!DOCTYPE html>
<html lang="en">
<head>
<meta charset="utf-8">
<title>Corvel Lane – Business Card</title>
<link href="https://fonts.googleapis.com/css2?family=Open+Sans:wght@400;600;700&display=swap" rel="stylesheet">
<style>
  :root {
    --ink: #111111;
    --brand-blue: #2b3990;
    --label-grey: #6d6e71;
    --card-white: #ffffff;
    --backdrop: #e9e9eb;
  }
  * { margin: 0; padding: 0; box-sizing: border-box; }
  html, body {
    width: 1200px;
    height: 1000px;
    overflow: hidden;
    background: var(--backdrop);
    font-family: "Open Sans", Arial, sans-serif;
  }
  .canvas {
    position: relative;
    width: 1200px;
    height: 1000px;
  }
  .business-card {
    position: absolute;
    left: 237px;
    top: 295px;
    width: 726px;
    height: 410px;
    background: var(--card-white);
    box-shadow: 0 2px 10px rgba(0, 0, 0, 0.12);
  }
  .company-name {
    position: absolute;
    left: 25px;
    top: 68px;
    font-size: 42px;
    font-weight: 700;
    line-height: 44px;
    color: var(--ink);
    letter-spacing: 0.5px;
    text-transform: uppercase;
  }
  .tagline {
    position: absolute;
    left: 25px;
    top: 120px;
    font-size: 12.5px;
    font-weight: 600;
    letter-spacing: 2.2px;
    color: var(--brand-blue);
    text-transform: uppercase;
    white-space: nowrap;
  }
  .name-band {
    position: absolute;
    left: 0;
    top: 289px;
    width: 272px;
    height: 87px;
    background: var(--brand-blue);
    border-radius: 0 43.5px 43.5px 0;
    color: var(--card-white);
    padding: 14px 0 0 30px;
  }
  .person-name {
    font-size: 28px;
    font-weight: 600;
    letter-spacing: 1.6px;
    line-height: 38px;
    white-space: nowrap;
  }
  .person-title {
    font-size: 14px;
    font-weight: 700;
    letter-spacing: 2.2px;
    line-height: 18px;
    text-transform: uppercase;
  }
  .contact-list {
    position: absolute;
    right: 43px;
    top: 308px;
    list-style: none;
    text-align: right;
    font-size: 15px;
    letter-spacing: 0.6px;
    line-height: 30px;
  }
  .contact-value { color: var(--brand-blue); }
  .contact-label { color: var(--label-grey); }
</style>
</head>
<body>
  <main class="canvas">
    <section class="business-card">
      <h1 class="company-name">Corvel Lane</h1>
      <p class="tagline">Public Transit Advocacy,Funding and Compliance.</p>

      <div class="name-band">
        <p class="person-name">Mark D Loyer</p>
        <p class="person-title">Director</p>
      </div>

      <ul class="contact-list">
        <li><span class="contact-value">(614) 380-2917</span> <span class="contact-label">(phone)</span></li>
        <li><span class="contact-value">markdloyer@vantomail.test</span> <span class="contact-label">(e-mail)</span></li>
      </ul>
    </section>
  </main>
</body>
</html>
```